Business Card and Stationary for Mentoring Co.
Dorlin Partners, LLC
Professional
Marguerite-Lou Dorlin
47 Kettrin Hollow Road
Durham, NH 03591
info@DorlinPartnersNH.example
www.DorlinPartnersNH.example
If we can get everything [logo, information and QR image on one side without it looking too busy that would be great otherwise the card will be two-sided
Would like the back of the business card to have a QRimage that links to the website when scanned.
This was a variation
this is the orginal design
This is variation #2
This is the QR code that takes you to my website when scanned by smart phone
Template for business card

```html
<!DOCTYPE html>
<html lang="en">
<head>
<meta charset="utf-8">
<title>Dorlin Partners, LLC — Stationery</title>
<link rel="stylesheet" href="https://fonts.googleapis.com/css2?family=Cinzel:wght@600&family=Open+Sans:wght@400;600&display=swap">
<style>
:root{
  --stage:#ebe8e3;
  --paper:#ffffff;
  --ink:#2b2b2b;
  --muted:#7a7a7a;
  --gold:#b8923a;
  --black:#141414;
  --silver-a:#f4f4f4;
  --silver-b:#c9c9c9;
  --rule:#9a9a9a;
  --faint:rgba(184,146,58,.10);
}
*{box-sizing:border-box;margin:0;padding:0}
html,body{width:1200px;height:674px;overflow:hidden}
body{background:var(--stage);position:relative;font-family:"Open Sans",Arial,sans-serif;color:var(--ink)}
.label{position:absolute;font-size:7px;font-weight:600;color:var(--ink);text-align:center;white-space:nowrap}
.piece{position:absolute;box-shadow:0 2px 6px rgba(0,0,0,.25)}
.brand{font-family:"Cinzel",Georgia,serif;font-weight:600;color:var(--gold);letter-spacing:.04em;white-space:nowrap}

/* business cards */
.card{width:132px;height:86px;border-radius:4px;background:var(--paper)}
.card.dark{background:var(--black);color:#ddd}
.card .brand{position:absolute;font-size:8px}
.card .person{position:absolute;left:10px;top:44px;font-size:5px;line-height:1.5}
.card .person b{font-size:5.5px;color:var(--gold)}
.card.back .brand{left:0;right:0;top:38px;text-align:center;font-size:9px}
.card.back .tag{position:absolute;left:0;right:0;top:52px;text-align:center;font-size:4.5px;color:var(--muted)}

/* pages */
.page{width:355px;height:521px;background:var(--paper)}
.page .band{position:absolute;left:14px;right:14px;top:14px;height:52px;border-radius:4px;background:linear-gradient(var(--silver-a),var(--silver-b));display:flex;align-items:center;justify-content:center;flex-direction:column}
.page .band .brand{font-size:12px}
.page .band small{font-size:5px;color:var(--muted);margin-top:2px}
.page .mark{position:absolute;left:0;right:0;top:250px;text-align:center;font-family:"Cinzel",Georgia,serif;font-weight:600;font-size:44px;color:var(--faint)}
.page .foot{position:absolute;left:0;right:0;bottom:12px;text-align:center;font-size:5px;color:var(--muted)}
.fax-title{position:absolute;right:22px;top:84px;font-size:7px;font-weight:600}
.fax-grid{position:absolute;left:14px;top:90px;width:327px;border:1px solid var(--rule);display:grid;grid-template-columns:1fr 1fr}
.fax-grid div{height:18px;border-bottom:1px solid var(--rule);font-size:6px;padding:5px 4px}
.fax-grid div:nth-child(odd){border-right:1px solid var(--rule)}
.fax-grid div:nth-last-child(-n+2){border-bottom:0}
.fax-checks{position:absolute;left:14px;top:188px;display:flex;gap:14px;font-size:5.5px}
.fax-checks span::before{content:"";display:inline-block;width:6px;height:6px;border:1px solid var(--rule);margin-right:3px;vertical-align:-1px}

/* envelopes */
.envelope{width:389px;height:168px;background:var(--paper)}
.envelope .brand{position:absolute;left:18px;top:16px;font-size:10px}
.envelope .addr{position:absolute;left:18px;top:31px;font-size:5px;color:var(--muted)}
.envelope .mark{position:absolute;left:0;right:0;top:70px;text-align:center;font-family:"Cinzel",Georgia,serif;font-weight:600;font-size:28px;color:var(--faint)}
.env-back{width:389px;height:172px}
.env-back svg{position:absolute;inset:0}
.env-back .brand{position:absolute;left:0;right:0;top:28px;text-align:center;font-size:9px}
</style>
</head>
<body>

<!-- business cards -->
<div class="label" style="left:29px;top:26px;width:132px">Business Card (Front) Option 1</div>
<div class="piece card" style="left:29px;top:40px">
  <span class="brand" style="left:10px;top:14px">Dorlin Partners</span>
  <p class="person"><b>Marguerite-Lou Dorlin</b><br>47 Kettrin Hollow Road<br>Durham, NH 03591<br>info@DorlinPartnersNH.example</p>
</div>

<div class="label" style="left:173px;top:26px;width:132px">Business Card (Front) Option 2</div>
<div class="piece card dark" style="left:173px;top:40px">
  <span class="brand" style="left:10px;top:14px">Dorlin Partners</span>
  <p class="person"><b>Marguerite-Lou Dorlin</b><br>47 Kettrin Hollow Road<br>Durham, NH 03591<br>info@DorlinPartnersNH.example</p>
</div>

<div class="label" style="left:317px;top:26px;width:132px">Business Card (Back) Option 1</div>
<div class="piece card back" style="left:317px;top:40px">
  <span class="brand">Dorlin Partners</span>
  <p class="tag">www.DorlinPartnersNH.example</p>
</div>

<div class="label" style="left:461px;top:26px;width:132px">Business Card (Back) Option 2</div>
<div class="piece card dark back" style="left:461px;top:40px">
  <span class="brand">Dorlin Partners</span>
  <p class="tag">www.DorlinPartnersNH.example</p>
</div>

<!-- envelope front -->
<div class="label" style="left:763px;top:34px;width:418px">Envelope (Front)</div>
<div class="piece envelope" style="left:778px;top:48px">
  <span class="brand">Dorlin Partners</span>
  <p class="addr">47 Kettrin Hollow Road, Durham, NH 03591</p>
  <p class="mark">Dorlin Partners</p>
</div>

<!-- fax cover -->
<div class="label" style="left:29px;top:130px;width:355px">Fax Cover</div>
<div class="piece page" style="left:29px;top:144px">
  <div class="band"><span class="brand">Dorlin Partners, LLC</span><small>Mentoring Co.</small></div>
  <p class="fax-title">FAX</p>
  <div class="fax-grid">
    <div>To:</div><div>From:</div>
    <div>Fax:</div><div>Pages:</div>
    <div>Phone:</div><div>Date:</div>
    <div>Re:</div><div>CC:</div>
  </div>
  <div class="fax-checks"><span>Urgent</span><span>For Review</span><span>Please Comment</span><span>Please Reply</span><span>Please Recycle</span></div>
  <p class="mark">Dorlin Partners</p>
  <p class="foot">47 Kettrin Hollow Road | Durham, NH 03591 | P: 603-555-0148 | info@DorlinPartnersNH.example | www.DorlinPartnersNH.example</p>
</div>

<!-- letterhead -->
<div class="label" style="left:403px;top:130px;width:355px">Letterhead</div>
<div class="piece page" style="left:403px;top:144px">
  <div class="band"><span class="brand">Dorlin Partners, LLC</span><small>Mentoring Co.</small></div>
  <p class="mark">Dorlin Partners</p>
  <p class="foot">47 Kettrin Hollow Road | Durham, NH 03591 | P: 603-555-0148 | info@DorlinPartnersNH.example | www.DorlinPartnersNH.example</p>
</div>

<!-- envelope backs -->
<div class="label" style="left:792px;top:252px;width:389px">Envelope (Back) Option 1</div>
<div class="piece env-back" style="left:792px;top:264px">
  <svg viewBox="0 0 389 172" width="389" height="172">
    <rect width="389" height="172" fill="#fff"/>
    <polygon points="0,0 389,0 194,86" fill="#fafafa" stroke="#ccc"/>
  </svg>
  <span class="brand">Dorlin Partners</span>
</div>

<div class="label" style="left:792px;top:362px;width:389px">Envelope (Back) Option 2</div>
<div class="piece env-back" style="left:792px;top:374px">
  <svg viewBox="0 0 389 172" width="389" height="172">
    <defs><linearGradient id="silverFlap" x1="0" y1="0" x2="0" y2="1"><stop offset="0" stop-color="#f4f4f4"/><stop offset="1" stop-color="#bdbdbd"/></linearGradient></defs>
    <rect width="389" height="172" fill="#fff"/>
    <polygon points="0,0 389,0 194,86" fill="url(#silverFlap)" stroke="#aaa"/>
  </svg>
  <span class="brand">Dorlin Partners</span>
</div>

<div class="label" style="left:792px;top:468px;width:389px">Envelope (Back) Option 3</div>
<div class="piece env-back" style="left:792px;top:482px">
  <svg viewBox="0 0 389 172" width="389" height="172">
    <rect width="389" height="172" fill="#fff"/>
    <polygon points="0,0 389,0 194,86" fill="#141414"/>
  </svg>
  <span class="brand">Dorlin Partners</span>
</div>

</body>
</html>
```